Dovra's Spice Blend Dry Roasted and Freshly Ground Spices to create the Authentic and Aromatic Maur

I need a packaging design for a new company based in Kent called Dovra's Spice Blend. the size of the packaging will be for a 250gm bag.

I would like bright colours so that it can stand out from out the other products on a super market shelf

The packaging must have the list of ingredients on the back;

I.e. Ingredients;
Cumin
Coriander
Dried Red Chili
Cinnamon
Cloves
Cardamon
Black Peppercorn
Rice

Reason: Not enough designed to choose from. Dovra's Spice Blend, Dry Roasted and Freshly Ground Spices to create the Authentic and Aromatic flavour Please also add Turmeric to the ingredient list Thank you MarlaOunsworth

```html
<!DOCTYPE html>
<html lang="en">
<head>
<meta charset="utf-8">
<title>Dovra's Spice Blend – Curry Powder Label</title>
<link rel="stylesheet" href="https://fonts.googleapis.com/css2?family=Arimo:wght@400;700&family=Merriweather:wght@300;400&display=swap">
<style>
  :root {
    --leaf-green: #5aab32;
    --ink: #3b3b3b;
    --paper: #ffffff;
  }
  html, body {
    margin: 0;
    padding: 0;
    width: 1200px;
    height: 1200px;
    overflow: hidden;
    background: var(--paper);
  }
  .label {
    position: relative;
    width: 1200px;
    height: 1200px;
  }
  .label-frame {
    position: absolute;
    inset: 0;
    width: 1200px;
    height: 1200px;
  }
  .label-text {
    position: absolute;
    left: 0;
    width: 1200px;
    margin: 0;
    text-align: center;
    color: var(--ink);
  }
  .brand-name {
    top: 198px;
    font-family: "Merriweather", serif;
    font-weight: 400;
    font-size: 112px;
    line-height: 1;
    color: var(--paper);
    left: 30px;
  }
  .tagline {
    top: 412px;
    font-family: "Arimo", Arial, sans-serif;
    font-weight: 700;
    font-size: 25px;
    letter-spacing: 0.01em;
  }
  .product-name {
    top: 510px;
    font-family: "Merriweather", serif;
    font-weight: 300;
    font-size: 136px;
    line-height: 1;
    letter-spacing: 0.02em;
  }
  .product-type {
    top: 670px;
    font-family: "Merriweather", serif;
    font-weight: 300;
    font-size: 52px;
    line-height: 1;
    letter-spacing: 0.16em;
  }
  .ingredients {
    top: 800px;
    font-family: "Arimo", Arial, sans-serif;
  }
  .ingredients-heading {
    margin: 0 0 4px;
    font-weight: 400;
    font-size: 26px;
    line-height: 1.2;
  }
  .ingredients-list {
    margin: 0;
    font-size: 22px;
    line-height: 1.18;
  }
</style>
</head>
<body>
<main class="label">
  <svg class="label-frame" viewBox="0 0 720 720" aria-hidden="true">
    <defs>
      <clipPath id="label-inner">
        <path d="M184 80 L536 80 A30 30 0 0 0 572 114 L572 300 Q567 330 572 360 L572 550 A30 30 0 0 0 540 584 Q460 580 362 590 Q264 580 184 584 A30 30 0 0 0 150 550 L150 360 Q155 330 150 300 L150 114 A30 30 0 0 0 184 80 Z"/>
      </clipPath>
    </defs>
    <path class="outer-border" fill="none" stroke="var(--leaf-green)" stroke-width="5"
      d="M178 70 L542 70 A36 36 0 0 0 582 106 L582 300 Q576 330 582 360 L582 556 A36 36 0 0 0 546 594 Q460 590 362 600 Q264 590 178 594 A36 36 0 0 0 140 556 L140 360 Q146 330 140 300 L140 106 A36 36 0 0 0 178 70 Z"/>
    <g clip-path="url(#label-inner)">
      <rect class="header-band" x="140" y="70" width="450" height="171" fill="var(--leaf-green)"/>
      <path class="header-inline" fill="none" stroke="var(--paper)" stroke-width="2"
        transform="translate(361 333) scale(0.965) translate(-361 -333)"
        d="M184 80 L536 80 A30 30 0 0 0 572 114 L572 300 Q567 330 572 360 L572 550 A30 30 0 0 0 540 584 Q460 580 362 590 Q264 580 184 584 A30 30 0 0 0 150 550 L150 360 Q155 330 150 300 L150 114 A30 30 0 0 0 184 80 Z"/>
    </g>
    <g class="divider divider-top" stroke="var(--leaf-green)" stroke-width="2.5">
      <line x1="190" y1="300" x2="345" y2="300"/>
      <line x1="387" y1="300" x2="540" y2="300"/>
    </g>
    <rect x="178" y="294" width="14" height="12" rx="3" fill="var(--leaf-green)" role="img" aria-label="leaf flourish"/>
    <rect x="354" y="292" width="24" height="14" rx="5" fill="var(--leaf-green)" role="img" aria-label="scroll flourish"/>
    <rect x="538" y="294" width="14" height="12" rx="3" fill="var(--leaf-green)" role="img" aria-label="leaf flourish"/>
    <g class="divider divider-bottom" stroke="var(--leaf-green)" stroke-width="2.5">
      <line x1="195" y1="456" x2="350" y2="456"/>
      <line x1="392" y1="456" x2="545" y2="456"/>
    </g>
    <rect x="183" y="450" width="14" height="12" rx="3" fill="var(--leaf-green)" role="img" aria-label="leaf flourish"/>
    <rect x="359" y="448" width="24" height="14" rx="5" fill="var(--leaf-green)" role="img" aria-label="scroll flourish"/>
    <rect x="543" y="450" width="14" height="12" rx="3" fill="var(--leaf-green)" role="img" aria-label="leaf flourish"/>
  </svg>

  <h1 class="label-text brand-name">Dovra's</h1>
  <p class="label-text tagline">DRY ROASTED AND FRESHLY GROUND SPICES</p>
  <h2 class="label-text product-name">CURRY</h2>
  <p class="label-text product-type">POWDER</p>
  <section class="label-text ingredients">
    <h3 class="ingredients-heading">INGREDIENTS</h3>
    <p class="ingredients-list">CUMIN, CORIANDER, DRIED RED CHILLI<br>CINNAMON, CLOVES, CARADAMON<br>BLACK PEPPERCORN, RICE, TURMERIC</p>
  </section>
</main>
</body>
</html>
```